Tax & Accounting business needs business card design

Looking for a professional classy business card for a tax and accounting business. We offer quality, professional services to individuals and small businesses including tax preparation and planning, accounting and bookkeeping, payroll services, and business consulting.

I am an Enrolled Agent (EA) which is a Federally Licensed Tax Practitioner. I am licensed to represent taxpayers before the BTQ.

We want to stand out from all the other "boring" tax & accounting firms without being over the top.

We have a well established firm in one location and are now opening a second location.

Industry/Entity Type

Accounting

Requirements
Must have
• Logo
• Logo color scheme
• Both location addresses
• Front and back of card
• Please see my sample business card (attached) for location addresses, phone numbers, ect. Although you may get some inspiration from this sample card, this is my own unqualified and bad attempt at designing my own card which I'm not happy with.

```html
<!DOCTYPE html>
<html lang="en">
<head>
<meta charset="utf-8">
<title>Ledger &amp; Levy Partners LLC – Business Card</title>
<link rel="stylesheet" href="https://fonts.googleapis.com/css2?family=Roboto:wght@300;400;500&display=swap">
<style>
  :root {
    --backdrop: #e9e7e3;
    --card-white: #f4f4f3;
    --teal: #164f4f;
    --teal-text: #1d5a58;
    --ink: #3e4444;
    --on-teal: #e6efee;
    --on-teal-soft: #c9dbd9;
  }
  * { box-sizing: border-box; margin: 0; padding: 0; }
  html, body {
    width: 1200px; height: 900px; overflow: hidden;
    background: var(--backdrop);
    font-family: "Roboto", Arial, sans-serif;
  }
  .canvas { position: relative; width: 1200px; height: 900px; }

  .card {
    position: absolute; width: 700px; height: 400px;
    box-shadow: 0 6px 18px rgba(0,0,0,.18);
    overflow: hidden;
  }

  /* Front */
  .card-front { left: 250px; top: 40px; background: var(--card-white); color: var(--ink); }
  .brand {
    position: absolute; top: 40px; left: 0; right: 0;
    display: flex; align-items: center; justify-content: center; gap: 14px;
  }
  .brand-dot { width: 22px; height: 22px; border-radius: 50%; background: var(--teal); }
  .brand-name {
    font-weight: 500; color: var(--teal-text); font-size: 34px; line-height: 1.05;
    text-align: center; letter-spacing: .5px;
  }
  .services {
    position: absolute; top: 150px; left: 0; right: 0; text-align: center;
    font-size: 17px; line-height: 1.35; font-weight: 400;
  }
  .web-band {
    position: absolute; top: 282px; left: 0; right: 0; height: 34px;
    background: var(--teal); color: #fff; font-weight: 500; font-size: 17px;
    display: flex; align-items: center; justify-content: center; letter-spacing: .3px;
  }
  .licence {
    position: absolute; top: 326px; left: 0; right: 0; text-align: center;
    font-size: 15px; color: var(--ink);
  }
  .foot-band { position: absolute; bottom: 22px; left: 0; right: 0; height: 12px; background: var(--teal); }

  /* Back */
  .card-back { left: 250px; top: 470px; background: var(--teal); color: var(--on-teal); font-weight: 300; }
  .holder { position: absolute; left: 60px; top: 66px; }
  .holder-name { font-size: 32px; letter-spacing: 1.5px; font-weight: 300; }
  .holder-email { font-size: 18px; margin-top: 8px; color: var(--on-teal-soft); }
  .divider { position: absolute; left: 60px; right: 60px; top: 170px; height: 1px; background: var(--on-teal-soft); }
  .office { position: absolute; top: 204px; font-size: 19px; line-height: 1.3; }
  .office-santa-fe { left: 60px; }
  .office-albuquerque { left: 400px; }
  .phones { margin-top: 22px; }
  .phones dt { display: inline-block; width: 22px; }
  .phones dd { display: inline; }
  .phones div { margin-bottom: 2px; }
</style>
</head>
<body>
<main class="canvas">
  <section class="card card-front" aria-label="Card front">
    <div class="brand">
      <span class="brand-dot"></span>
      <div class="brand-name">LEDGER &amp; LEVY<br>PARTNERS LLC</div>
    </div>
    <p class="services">
      Professional Business Services<br>
      Taxes - Accounting - Bookkeeping - Payroll<br>
      for individuals and small businesses<br>
      Enrolled Agent - Federally Licensed Tax Practitioner
    </p>
    <div class="web-band">www.ledgerlevy-nm.com</div>
    <p class="licence">Licensed to Represent Taxpayers Before the BTQ</p>
    <div class="foot-band"></div>
  </section>

  <section class="card card-back" aria-label="Card back">
    <div class="holder">
      <h1 class="holder-name">MARISOL T. VEGA, EA</h1>
      <p class="holder-email">marisol@ledgerlevyabq.com</p>
    </div>
    <div class="divider"></div>
    <address class="office office-santa-fe" style="font-style:normal">
      Santa Fe Office<br>480 Canyon Mesa Rd Ste B<br>Santa Fe, NM 87507
      <dl class="phones">
        <div><dt>t</dt><dd>505 555 0146</dd></div>
        <div><dt>f</dt><dd>505 555 0147</dd></div>
      </dl>
    </address>
    <address class="office office-albuquerque" style="font-style:normal">
      Albuquerque Office<br>3620 Mesa Verde Ave NE<br>Albuquerque, NM 87110
      <dl class="phones">
        <div><dt>t</dt><dd>505 555 0188</dd></div>
        <div><dt>f</dt><dd>505 555 0177</dd></div>
      </dl>
    </address>
  </section>
</main>
</body>
</html>
```